Flyer To Solicit Donations for a Good Cause

Hi. I am running the distance of a marathon race to solicit donations for a charitable cause. I need a well designed flyer to help me solicit support from friends and others. The copy for the flyer is attached. There is a significant amount of written text so it will need to be laid out in a way that is easy to read but also mixes well with some good images and design appeal. I am open to creative ideas. I have also attached my photo and a photo of me shaking hands with Mayor Derlin of Delphi and president of the Brastow Harmonic Fellowship. Also there are some photos of the areas. These photos don't have to be used except for the one of me shaking hands with the Mayor and a caption underneath it. Otherwise, I am open to other stock photos or graphics. Feel free to contact me if you have questions. Thank you !

Update: ONE SIDED FLYER

• Photo of the Mayor and Toby with the caption identifying us; All of the copy/text.

```html
<!DOCTYPE html>
<html lang="en">
<head>
<meta charset="utf-8">
<title>A Special Journey For Your Specific Prayers</title>
<link rel="stylesheet" href="https://fonts.googleapis.com/css2?family=Archivo+Black&family=Arimo:wght@400;700&family=Dancing+Script:wght@500&display=swap">
<style>
  :root {
    --title-blue: #1e8fd2;
    --rule-blue: #6fb6e3;
    --body-ink: #3a3a3a;
    --script-ink: #4a4a4a;
    --paper: #ffffff;
    --suit-dark: #2b2f38;
    --shirt-light: #e9ecef;
    --sky-blue: #9cc6e4;
    --stone-warm: #c9b79a;
  }
  * { margin: 0; padding: 0; box-sizing: border-box; }
  html, body { width: 849px; height: 1200px; overflow: hidden; background: var(--paper); }
  .flyer {
    position: relative;
    width: 849px;
    height: 1200px;
    overflow: hidden;
    background: var(--paper);
    font-family: "Arimo", Arial, sans-serif;
    color: var(--body-ink);
  }
  .headline {
    position: absolute;
    left: 40px; right: 40px; top: 18px;
    text-align: center;
    font-family: "Archivo Black", "Arial Black", sans-serif;
    color: var(--title-blue);
    font-size: 29px;
    line-height: 1.22;
    padding: 6px 0 8px;
    border-top: 2px solid var(--rule-blue);
    border-bottom: 2px solid var(--rule-blue);
  }
  .copy {
    position: absolute;
    left: 57px; right: 50px; top: 132px;
    font-size: 16.4px;
    line-height: 1.45;
  }
  .copy p { margin-bottom: 22px; }
  .steps { list-style: none; }
  .steps li {
    position: relative;
    padding-left: 22px;
    margin-bottom: 22px;
  }
  .steps li::before {
    content: "";
    position: absolute;
    left: 3px; top: 9px;
    width: 6px; height: 6px;
    border-radius: 50%;
    background: var(--body-ink);
  }
  .runner-photo {
    position: absolute;
    left: 690px; top: 900px;
    width: 159px; height: 300px;
    background: linear-gradient(160deg, var(--paper) 0%, var(--shirt-light) 40%, var(--suit-dark) 100%);
    z-index: 1;
  }
  .tagline {
    position: absolute;
    left: 240px; top: 985px;
    width: 450px;
    text-align: center;
    font-family: "Dancing Script", cursive;
    color: var(--script-ink);
    font-size: 25px;
    line-height: 1.35;
    z-index: 2;
  }
  .tagline .tagline-end { display: block; text-align: right; padding-right: 20px; }
  .handshake-photo {
    position: absolute;
    left: 50px; top: 962px;
    width: 205px; height: 190px;
    border-radius: 50%;
    background: linear-gradient(180deg, var(--sky-blue) 0%, var(--shirt-light) 45%, var(--stone-warm) 100%);
  }
  .caption {
    position: absolute;
    left: 30px; top: 1168px;
    font-size: 11px;
    color: var(--body-ink);
  }
</style>
</head>
<body>
<main class="flyer">
  <h1 class="headline">A Special Journey For Your Specific Prayers<br>&amp; For An Important Ancient Cause</h1>

  <section class="copy">
    <p>This coming April 2016 Toby Hallstrom will make a special running journey of 26 miles through the ancient lands of Apollo and Athena at Delphi on Mt. Parnassus in Greece.</p>
    <p>Toby will adorn his running outfit with special cloth strips that will contain written prayers and petitions of people who will sponsor his journey by making a charitable donation to the Brastow Harmonic Fellowship, an organization that preserves the land and the Delphic culture. www.harmonic-fellowship-committee.org</p>
    <p>The concept is simple and very powerful: as Toby runs, your written prayer on a cloth strip will flow and emanate in the wind &mdash; being blessed by the spirits of this ancient and magical land &mdash; asking unto the wind that your prayer be answered. This type of prayer practice dates back to ancient times. The Tibetan culture commonly uses prayer flags with special mantras and symbols.</p>
    <p>Will you make a prayer for yourself or a loved one and support a good cause?<br>Here is how to get your prayer started:</p>
    <ul class="steps">
      <li>Decide what you want your prayer, petition or intention to be.</li>
      <li>Define your prayer, petition or intention by writing it down.</li>
      <li>Refine it is concise, clear &amp; specific. (18 words or less is ideal for each strip cloth).</li>
      <li>Contact Toby at toby@hallstromvale.com and tell him how many prayer cloth strips you wish to obtain. Toby will then send you the cloth for you to write your prayer and send back to him or he will write out the prayer for you. Toby can also answer any questions you may have.</li>
      <li>A minimum donation of $50 for each prayer cloth is requested. Checks can be made to the &ldquo;Hallstrom Vale Trust Account/Brastow Harmonic Fellowship&rdquo; and mail to Toby Hallstrom, Hallstrom Vale PLC, 4125 Linden Avenue, Ste. 210 Lakemoor, Ohio 44012 or through online payment instructions sent by email from Toby as requested.</li>
    </ul>
  </section>

  <div class="runner-photo" role="img" aria-label="Portrait photo of Toby in a dark suit and white shirt"></div>

  <p class="tagline">Your Prayer Can Make A Difference For You<span class="tagline-end">&amp; For A Good Cause !</span></p>

  <div class="handshake-photo" role="img" aria-label="Photo of Toby shaking hands with Mayor Derlin outdoors"></div>
  <p class="caption">Mayor Derlin of Delphi and president of the Brastow Harmonic Fellowship.</p>
</main>
</body>
</html>
```